Halcyon Motion - Personal & Rehab Training

Business Card for my personal training business - Halcyon Motion. I focus on personal and rehab training. I would like a double sided card, round edges. front of card will be my existing logo and the back will have an image (black and white or exercise, people exercising, weights, etc) along with my name and details. Such as:
Tamsin Vereker
Personal & Rehab Trainer
www.halcyonmotion-example.com.au
0491583026
I have some images that I have downloaded that I am happy to send to the designer.
Thanks
Target Market(s)
athletes, middle to high income, sport related
Contact Information for Business Card
Tamsin Vereker
Personal & Rehab Trainer
0491583026
Colors
Designer to choose only greyscale colors for use in the design.
Requirements
Must have
- my existing logo
Nice to have
- one of the images uploaded. I really like the girl with the mint coloured shoes as this is one of my logo colours

```html
<!DOCTYPE html>
<html lang="en">
<head>
<meta charset="utf-8">
<title>Halcyon Motion – Business Card</title>
<link href="https://fonts.googleapis.com/css2?family=Roboto:wght@300;400;700&display=swap" rel="stylesheet">
<style>
  :root {
    --backdrop: #1f2125;
    --card-front: #262b35;
    --card-back: #25272b;
    --ink-light: #f1f2f4;
    --ink-soft: #c9ccd1;
    --photo-dark: #2b2d31;
    --photo-mid: #8d9096;
    --photo-light: #c7c9cc;
  }
  * { margin: 0; padding: 0; box-sizing: border-box; }
  html, body {
    width: 1200px;
    height: 750px;
    overflow: hidden;
    background: var(--backdrop);
    font-family: "Roboto", Arial, sans-serif;
  }
  .canvas {
    position: relative;
    width: 1200px;
    height: 750px;
  }
  .card {
    position: absolute;
    top: 225px;
    width: 520px;
    height: 300px;
    border-radius: 18px;
    overflow: hidden;
  }
  .card--front {
    left: 40px;
    background: var(--card-front);
    display: flex;
    align-items: center;
    justify-content: center;
  }
  .card--back {
    left: 640px;
    background: var(--card-back);
  }
  .brand {
    display: flex;
    align-items: center;
    gap: 16px;
    color: var(--ink-light);
    font-weight: 400;
    letter-spacing: 0.14em;
    text-transform: uppercase;
  }
  .brand__square {
    border: 3px solid var(--ink-light);
    border-radius: 8px;
  }
  .card--front .brand { font-size: 34px; }
  .card--front .brand__square { width: 56px; height: 56px; }
  .card--back .brand {
    position: absolute;
    left: 30px;
    top: 40px;
    font-size: 20px;
    gap: 10px;
  }
  .card--back .brand__square { width: 34px; height: 34px; border-width: 2px; border-radius: 5px; }
  .card__photo {
    position: absolute;
    top: 0;
    right: 0;
    width: 300px;
    height: 100%;
    background:
      linear-gradient(90deg, var(--card-back) 0%, rgba(37,39,43,0) 22%),
      radial-gradient(ellipse at 45% 45%, var(--photo-light) 0%, var(--photo-mid) 40%, var(--photo-dark) 100%);
  }
  .contact {
    position: absolute;
    left: 36px;
    top: 150px;
    color: var(--ink-light);
  }
  .contact__name { font-size: 19px; font-weight: 700; }
  .contact__role { font-size: 14px; font-weight: 300; color: var(--ink-soft); margin-top: 2px; }
  .contact__phone { font-size: 14px; font-weight: 300; margin-top: 26px; padding-left: 14px; }
  .contact__web {
    position: absolute;
    right: 22px;
    bottom: 20px;
    font-size: 11px;
    font-weight: 400;
    color: var(--ink-light);
  }
</style>
</head>
<body>
  <main class="canvas">
    <section class="card card--front" aria-label="Card front">
      <div class="brand">
        <span class="brand__square"></span>
        <span class="brand__name">Halcyon Motion</span>
      </div>
    </section>

    <section class="card card--back" aria-label="Card back">
      <div class="card__photo" role="img" aria-label="Black and white photo of athletes training with a climbing rope in a gym"></div>
      <div class="brand">
        <span class="brand__square"></span>
        <span class="brand__name">Halcyon Motion</span>
      </div>
      <div class="contact">
        <p class="contact__name">Tamsin Vereker</p>
        <p class="contact__role">Personal &amp; Rehab Trainer</p>
        <p class="contact__phone">0491583026</p>
      </div>
      <p class="contact__web">www.halcyonmotion-example.com.au</p>
    </section>
  </main>
</body>
</html>
```